Website re-design wedding music business

I need my wordpress wedding music website redesigned. I'm a wedding pianist and also provide duo/trio entertainment with other musicians and looking for an overhaul of my wordpress site.

Website: tomaslevett.com.au

Target Market(s)

brides; engaged couples

Industry/Entity Type

Wedding

Number of Pages Required

5+ page

Colors

Designer to choose colors to be used in the design.

Requirements
Must have
• I'm looking to overhaul my website which is looking rather tired after 4 years. It is functional but not inviting to visitors. Initially my website started out as a solo piano player providing music for wedding. It is gradually growing now where brides can book
• 1) Solo Piano
• 2) Duo (any combination of Piano / Cello / Vocalist / Violin)
• 3) Trio (any combination of Piano/ Cello /Vocalist / Violin)
• in future it may increase to 4 / 5 /6 piece bands so that needs to be taken into account for the future growth where I'll recruit other musicians.
• Some other functionality I'd like to see
• - Visitors want a calendar to know availability of musicians
• - Automatically providing enquiry price & discount (if applicable)
• - Automating the booking form process (manual) - There's a PDF form I send to the customer after we go back/forth on email on songs/price etc but if more of it could be automated online that would be great. If move to online it would be good to be able to override the set prices with a custom price and also providing a payment gateway
• More Flexibility on pricing - customer selects type of artists they want and it calculates a price based on who they have chosen whether it is a ceremony or canapes or reception (or combination of any). Extra transport fee is added if >50km out of Melbourne.
• How would you re-design this website. Imagine you are a bride/groom looking to book wedding music services. I would love to see some concepts .
• Please indicate any other fees required for your submission and level of support post this competition. I would like this to be an on-going relationship.
Nice to have
• I'd preferably like the website to be in wordpress as I've been familiar with it over time and can do basic updates in the back end. Happy for other suggestions if you can convince me I should move away from wordpress.

```html
<!DOCTYPE html>
<html lang="en">
<head>
<meta charset="utf-8">
<title>Tomas Levett – Wedding & Event Pianist</title>
<link rel="stylesheet" href="https://fonts.googleapis.com/css2?family=Great+Vibes&family=Lora:ital@1&family=Source+Sans+3:wght@400;600;700&display=swap">
<style>
:root{
  --gold:#b9975b;
  --gold-dark:#9d7d45;
  --ink:#2b2725;
  --dark:#1d1a19;
  --text:#555;
  --muted:#888;
  --light:#efefef;
  --panel:#f3f3f3;
  --white:#fff;
}
*{box-sizing:border-box;margin:0;padding:0}
html,body{width:1200px;height:4027px;overflow:hidden}
body{font-family:"Source Sans 3",Arial,sans-serif;color:var(--text);background:var(--white);font-size:13px;line-height:1.5}
.wrap{width:980px;margin:0 auto;position:relative}
section,header,footer{position:relative;overflow:hidden}
.h2{font-weight:700;font-size:20px;color:var(--ink);text-transform:uppercase;letter-spacing:.3px}
.btn{display:inline-block;font-weight:700;font-size:15px;text-transform:uppercase;padding:14px 0;width:172px;text-align:center;letter-spacing:.4px}
.btn-gold{background:var(--gold);color:#fff}
.btn-white{background:#fff;color:var(--ink)}
.btn-dark{background:var(--dark);color:#fff}
.more{font-weight:700;font-size:11px;color:var(--ink);text-transform:uppercase;margin-top:14px;display:block}

.topbar{height:24px;background:var(--dark)}
.topbar ul{list-style:none;display:flex;justify-content:flex-end;gap:14px;height:24px;align-items:center;color:#bbb;font-size:10px;text-transform:uppercase}
.site-header{height:105px;background:#fff}
.site-header .wrap{display:flex;align-items:center;height:105px;justify-content:space-between}
.brand{display:flex;align-items:center;gap:12px}
.brand-dot{width:44px;height:44px;border-radius:50%;background:var(--ink)}
.brand-name{font-weight:700;font-size:19px;color:var(--ink);letter-spacing:.5px;line-height:1.1}
.brand-sub{font-size:13px;color:var(--ink)}
.main-nav{display:flex;gap:26px;font-weight:700;font-size:13px;color:var(--ink);text-transform:uppercase}

.hero{height:515px;background:linear-gradient(100deg,#3c4a2a 0%,#6f7850 35%,#a9a9a0 55%,#6a7449 80%,#3b4726 100%)}
.hero-photo{position:absolute;inset:0}
.hero-copy{position:absolute;left:0;right:0;top:36px;text-align:center;color:#fff}
.hero-title{font-family:"Great Vibes",cursive;font-size:80px;line-height:1;font-weight:400}
.hero-sub{font-size:20px;margin-top:6px}
.hero-text{width:300px;margin:12px auto 0;font-size:14px;line-height:1.45}
.hero .btn{margin-top:26px;width:140px}

.awards{height:116px;background:var(--light)}
.awards .wrap{display:flex;align-items:center;height:116px}
.awards-quote{font-weight:700;font-size:17px;color:var(--ink);text-align:center;width:460px;margin-left:90px;line-height:1.3}
.badges{display:flex;gap:30px;margin-left:120px}
.badge{width:66px;height:66px;border-radius:50%;background:#3a3532;border:4px solid var(--gold)}
.badge.alt{background:#d9d3c4;border-color:#8e8a82}

.about{height:314px}
.about .wrap{display:flex;padding-top:42px}
.about-col{width:50%;padding-right:36px}
.about-col+.about-col{border-left:1px solid #ddd;padding:0 0 0 30px}
.about-col p{margin-top:14px;font-size:13px;line-height:1.55;color:#666}
.about-col p+p{margin-top:4px}

.when{height:322px;background:#fff}
.when-band{position:absolute;left:0;right:0;top:0;height:200px;background:linear-gradient(180deg,#1c2415 0%,#2f3824 60%,#3e4630 100%)}
.when-curve{position:absolute;left:0;top:130px}
.when-title{position:absolute;top:52px;left:0;right:0;text-align:center;color:#fff;font-weight:700;font-size:19px}
.occasions{position:absolute;top:134px;left:0;right:0;display:flex;justify-content:center;gap:66px}
.occasion{width:104px;text-align:center}
.occasion-icon{width:104px;height:104px;border-radius:50%;background:var(--ink);border:4px solid #fff;box-shadow:0 0 0 2px var(--gold);display:flex;align-items:center;justify-content:center}
.occasion-icon.active{background:var(--gold)}
.occasion-label{margin-top:16px;font-weight:700;font-size:12px;color:var(--ink);text-transform:uppercase;line-height:1.25}

.media{height:537px}
.media .wrap{display:flex;gap:28px;padding-top:30px}
.media-video{width:642px}
.media-music{width:310px}
.media .h2{margin-bottom:14px}
.video-frame{height:390px;background:linear-gradient(135deg,#4c5a36,#7c8764 45%,#b7b4a8 60%,#50593a);display:flex;align-items:center;justify-content:center}
.player{height:390px;background:#fff;border:1px solid #e2e2e2}
.player-art{height:118px;background:linear-gradient(90deg,#1f1f1f,#6a6a6a 60%,#e9e9e9);position:relative}
.player-play{position:absolute;left:150px;top:30px;width:44px;height:44px;border-radius:50%;background:var(--gold)}
.tracks{list-style:none;padding:6px 8px}
.tracks li{display:flex;justify-content:space-between;font-size:10px;color:#555;padding:3px 0;border-bottom:1px solid #f0f0f0;text-transform:uppercase;white-space:nowrap}
.tracks li span:first-child{padding-left:30px;position:relative}
.tracks li span:first-child::before{content:"";position:absolute;left:0;top:1px;width:22px;height:12px;background:#777}
.player-foot{display:flex;gap:8px;padding:8px;font-size:10px;color:#333;border-top:1px solid #eee}
.player-foot i{width:30px;height:30px;background:#555;display:block}

.types{height:470px;background:linear-gradient(180deg,#1b1816,#2c2623 60%,#1b1816)}
.types-title{text-align:center;color:#fff;font-weight:700;font-size:19px;padding-top:45px}
.type-grid{display:flex;gap:22px;justify-content:center;margin-top:26px}
.type-card{width:228px;height:228px;position:relative}
.type-card b{position:absolute;left:14px;bottom:12px;color:#fff;font-size:14px;text-transform:uppercase}
.type-actions{display:flex;justify-content:center;gap:14px;margin-top:42px}

.why{height:403px}
.why-photo{position:absolute;right:0;top:0;width:520px;height:403px;background:linear-gradient(90deg,#fff 0%,#e6e6e6 30%,#9a9a9a 60%,#cfcfcf 85%,#fff 100%)}
.why .wrap{padding-top:50px}
.features{display:grid;grid-template-columns:300px 300px;gap:40px 60px;margin-top:30px}
.feature{display:flex;gap:18px}
.feature svg{flex:none}
.feature h3{font-size:13px;font-weight:700;color:var(--ink);text-transform:uppercase}
.feature p{font-size:12px;color:#777;line-height:1.5}

.info{height:583px}
.info .wrap{display:flex;gap:24px;padding-top:34px}
.info-col{width:310px}
.info-col .h2{margin-bottom:16px}
.box{background:var(--panel);height:460px;padding:18px 20px}
.event{margin-bottom:22px}
.event-date{display:inline-block;background:var(--gold);color:#fff;font-size:9px;font-weight:700;padding:1px 6px}
.event h4{font-size:14px;color:var(--ink);text-transform:uppercase;line-height:1.2;margin-top:3px}
.event p{font-size:12px;color:#666}
.all-events{display:block;text-align:center;font-weight:700;font-size:11px;color:var(--ink);margin-top:8px}
.testimonial{background:#fff;text-align:center;padding:22px 22px;height:460px}
.quote-mark{font-family:Georgia,serif;font-size:56px;color:var(--gold);line-height:.7;height:34px}
.testimonial blockquote{font-family:"Lora",Georgia,serif;font-style:italic;font-size:14px;color:#444;line-height:1.55;margin-top:10px}
.testimonial cite{display:block;font-style:normal;font-weight:700;font-size:13px;color:var(--ink);margin-top:18px}
.testimonial small{font-size:12px;color:#777}
.dots{display:flex;gap:6px;justify-content:center;margin-top:18px}
.dots i{width:10px;height:10px;border-radius:50%;border:1px solid #aaa}
.dots i:first-child{background:var(--gold);border-color:var(--gold)}
.enquiry p{font-size:12px;color:#666;margin-bottom:12px}
.field{background:#fff;border:1px solid #ddd;height:34px;margin-bottom:9px;font-size:12px;color:#999;padding:7px 10px}
.field.tall{height:90px}
.enquiry .btn{width:100%;margin-top:4px}

.hire{height:222px;background:linear-gradient(180deg,#dcdcdc,#c8c8c8 50%,#e4e4e4);text-align:center}
.hire h2{font-weight:700;font-size:20px;color:var(--ink);padding-top:36px}
.hire p{font-size:15px;color:#444;margin-top:4px}
.hire-actions{display:flex;justify-content:center;gap:14px;margin-top:26px}

.site-footer{height:416px;background:var(--ink);color:#bbb}
.footer-cols{display:flex;padding-top:40px}
.footer-brand{width:340px}
.footer-brand .brand-name,.footer-brand .brand-sub{color:#fff}
.footer-brand .brand-dot{background:#fff}
.footer-brand address{font-style:normal;font-size:11px;margin-top:14px;line-height:1.5}
.footer-brand address span{display:block;margin-top:10px}
.footer-links{width:340px}
.footer-links h4,.footer-gram h4{color:#fff;font-size:12px;text-transform:uppercase;font-weight:700;margin-bottom:8px}
.footer-links .lists{display:flex;gap:60px}
.footer-links ul{list-style:none;font-size:11px;line-height:1.6}
.footer-gram{width:300px}
.footer-gram h4{display:flex;justify-content:space-between}
.footer-gram h4 span{color:var(--gold);font-weight:400;text-transform:none}
.gram{display:grid;grid-template-columns:repeat(3,1fr);gap:4px}
.gram div{height:72px;background:linear-gradient(135deg,#5a4f45,#8c7d6c)}
.gram div:nth-child(2n){background:linear-gradient(135deg,#3d3733,#7a6e62)}
.socials{display:flex;justify-content:center;gap:30px;margin-top:44px;border-top:1px solid #3e3936;padding-top:20px;font-size:12px;color:#ccc}
.socials span{display:flex;align-items:center;gap:8px}
.socials i{width:28px;height:28px;border-radius:50%;border:2px solid var(--gold);display:block}
.legal{display:flex;justify-content:space-between;align-items:flex-end;margin-top:34px;font-size:11px}
.cards{display:flex;gap:6px}
.cards span{background:#fff;color:var(--ink);font-weight:700;font-size:10px;width:52px;height:30px;display:flex;align-items:center;justify-content:center}
</style>
</head>
<body>

<div class="topbar">
  <ul class="wrap"><li>Home</li><li>Contact</li><li>Videogram</li><li>Suppliers</li><li>Hire Baby Grand Piano</li><li>FAQs</li></ul>
</div>

<header class="site-header">
  <div class="wrap">
    <div class="brand">
      <span class="brand-dot"></span>
      <div><div class="brand-name">TOMAS LEVETT</div><div class="brand-sub">Wedding &amp; Event Pianist</div></div>
    </div>
    <nav class="main-nav"><span>About Tomas</span><span>Events</span><span>Music</span><span>Video</span><span>Repertoire</span><span>Prices</span><span>Gallery</span><span>Testimonials</span><span>Buy CD</span></nav>
  </div>
</header>

<section class="hero">
  <div class="hero-photo" role="img" aria-label="Pianist at a white grand piano and a cellist performing outdoors among trees"></div>
  <div class="hero-copy">
    <h1 class="hero-title">Tomas Levett</h1>
    <div class="hero-sub">Wedding Pianist | Event Pianist</div>
    <p class="hero-text">Tomas Levett is Melbourne's premier award winning wedding &amp; event pianist specialising in playing beautiful background music for weddings, special occasions &amp; corporate events.</p>
    <span class="btn btn-gold">Book Now</span>
  </div>
</section>

<section class="awards">
  <div class="wrap">
    <p class="awards-quote">“ Southern Bridal Awards 2016 Award for<br>Best Victorian Supplier for Ceremony Music ”</p>
    <div class="badges"><span class="badge"></span><span class="badge"></span><span class="badge alt"></span></div>
  </div>
</section>

<section class="about">
  <div class="wrap">
    <div class="about-col">
      <h2 class="h2">About Us</h2>
      <p>Tomas Levett is a Melbourne professional pianist with over 5 years experience within the wedding industry and has played piano for more than 30 years.</p>
      <p>Tomas is also excited from April 2017 to provide a portable baby grand piano available in white to provide that 'wow' factor for your event (additional cost to hire). With a wide and varied repertoire Tomas can provide the perfect background to complement your event. To discuss how he can meet your event please use the contact form for a no-obligation quotation.</p>
      <span class="more">Read More Bios ▸</span>
    </div>
    <div class="about-col">
      <h2 class="h2">Repertoire</h2>
      <p>Duis sed odio sit amet nibh vulputate cursus a sit amet mauris. Morbi accumsan ipsum velit. Nam nec tellus a odio tincidunt auctor a ornare odio. Sed non mauris vitae erat consequat auctor eu in elit. Class aptent taciti sociosqu ad litora torquent per conubia nostra, per inceptos himenaeos. Mauris in erat justo. Nullam ac urna eu felis dapibus condimentum sit amet a augue. Sed non neque elit. Sed ut imperdiet nisi. Proin condimentum fermentum nunc.</p>
      <span class="more">Read More Repertoire ▸</span>
    </div>
  </div>
</section>

<section class="when">
  <div class="when-band" role="img" aria-label="Dark garden scene with a white piano"></div>
  <svg class="when-curve" width="1200" height="80" viewBox="0 0 1200 80"><path d="M0 80 Q600 -40 1200 80 Z" fill="#fff"/></svg>
  <h2 class="when-title">WHEN DOES A PIANIST PLAY?</h2>
  <div class="occasions">
    <div class="occasion"><div class="occasion-icon"><svg width="50" height="40" viewBox="0 0 50 40" fill="none" stroke="#fff" stroke-width="2.5"><circle cx="18" cy="24" r="12"/><circle cx="32" cy="24" r="12"/></svg></div><div class="occasion-label">Wedding<br>Ceremony</div></div>
    <div class="occasion"><div class="occasion-icon"><svg width="50" height="40" viewBox="0 0 50 40" fill="none" stroke="#fff" stroke-width="2.5"><circle cx="14" cy="12" r="5"/><circle cx="36" cy="12" r="5"/><circle cx="25" cy="10" r="6"/><path d="M6 36v-8a8 8 0 0 1 16 0M28 36v-8a8 8 0 0 1 16 0M16 36v-6a9 9 0 0 1 18 0"/></svg></div><div class="occasion-label">Corporate<br>Events</div></div>
    <div class="occasion"><div class="occasion-icon active"><svg width="50" height="44" viewBox="0 0 50 44" fill="none" stroke="#fff" stroke-width="2.5"><rect x="8" y="26" width="34" height="14"/><rect x="13" y="14" width="24" height="12"/><path d="M25 4v8"/></svg></div><div class="occasion-label">Anniversaries<br>(e.g. Birthdays)</div></div>
    <div class="occasion"><div class="occasion-icon"><svg width="50" height="44" viewBox="0 0 50 44" fill="none" stroke="#fff" stroke-width="2.5"><path d="M10 6h12l-2 14a4 4 0 0 1-8 0zM16 24v14M11 38h10M28 6h12l-2 14a4 4 0 0 1-8 0zM34 24v14M29 38h10"/></svg></div><div class="occasion-label">Canapés &amp;<br>Receptions</div></div>
    <div class="occasion"><div class="occasion-icon"><svg width="50" height="44" viewBox="0 0 50 44" fill="none" stroke="#fff" stroke-width="2.5"><circle cx="20" cy="12" r="7"/><path d="M20 19v20M30 10v18M40 6v18M30 10l10-4"/><circle cx="27" cy="29" r="3"/><circle cx="37" cy="25" r="3"/></svg></div><div class="occasion-label">Accompanist<br>for Singers</div></div>
    <div class="occasion"><div class="occasion-icon"><svg width="50" height="40" viewBox="0 0 50 40" fill="none" stroke="#fff" stroke-width="2.5"><path d="M6 12q19 -6 38 0q0 16 -12 18q-7 0 -7 -6q0 6 -7 6q-12 -2 -12 -18z"/></svg></div><div class="occasion-label">Special<br>Events</div></div>
  </div>
</section>

<section class="media">
  <div class="wrap">
    <div class="media-video">
      <h2 class="h2">Video</h2>
      <div class="video-frame" role="img" aria-label="Video still of the pianist at a white grand piano in a garden">
        <svg width="70" height="70" viewBox="0 0 70 70"><circle cx="35" cy="35" r="32" fill="none" stroke="#fff" stroke-width="4"/><path d="M28 22l20 13-20 13z" fill="#fff"/></svg>
      </div>
    </div>
    <div class="media-music">
      <h2 class="h2">Music</h2>
      <div class="player">
        <div class="player-art" role="img" aria-label="Close-up of piano keys"><span class="player-play"></span></div>
        <ul class="tracks">
          <li><span>Northwind - Morning Light</span><span>2,081</span></li>
          <li><span>Juno Park - Lucky Day</span><span>1,902</span></li>
          <li><span>Harlan Reed - Always You</span><span>1,640</span></li>
          <li><span>Open Rooms - Quiet Garden</span><span>1,322</span></li>
          <li><span>Silver Tide - Blue Harbour</span><span>1,208</span></li>
          <li><span>Miles Garner Band - Slow Dance</span><span>998</span></li>
          <li><span>Arlo Grant - Evening Star</span><span>874</span></li>
        </ul>
        <div class="player-foot"><i></i><div>Tomas Levett Piano<br><b>Wedding Piano Background</b></div></div>
      </div>
    </div>
  </div>
</section>

<section class="types">
  <h2 class="types-title">WHAT TYPE OF MUSIC DO YOU NEED?</h2>
  <div class="type-grid">
    <div class="type-card" role="img" aria-label="Solo pianist at a grand piano" style="background:linear-gradient(160deg,#5e6b42,#2f3323)"><b>Solo Piano</b></div>
    <div class="type-card" role="img" aria-label="Piano and vocalist duo" style="background:linear-gradient(160deg,#7b6a55,#3a302a)"><b>Duo</b></div>
    <div class="type-card" role="img" aria-label="Trio with cellist" style="background:linear-gradient(160deg,#6b7a8a,#2f3640)"><b>Trio</b></div>
    <div class="type-card" role="img" aria-label="Larger ensemble of musicians" style="background:linear-gradient(160deg,#7a5a42,#2e2520)"><b>Something Else</b></div>
  </div>
  <div class="type-actions"><span class="btn btn-gold">Book Now</span><span class="btn btn-white">Get Your Price List</span></div>
</section>

<section class="why">
  <div class="why-photo" role="img" aria-label="Soft black and white photo of the musicians, fading into white"></div>
  <div class="wrap">
    <h2 class="h2">Why Choose Our Service</h2>
    <div class="features">
      <div class="feature"><svg width="38" height="38" viewBox="0 0 38 38" fill="none" stroke="#b9975b" stroke-width="2"><ellipse cx="19" cy="21" rx="14" ry="10"/><path d="M14 11h8M10 30v4M28 30v4"/></svg><div><h3>You Save Money</h3><p>Nam nec tellus a odio tincidunt auctor sed non elit eu mauris vitae erat as well consequat auctor eu in elit.</p></div></div>
      <div class="feature"><svg width="38" height="38" viewBox="0 0 38 38" fill="none" stroke="#b9975b" stroke-width="2"><circle cx="19" cy="19" r="15"/><circle cx="14" cy="15" r="1.5" fill="#b9975b"/><circle cx="24" cy="15" r="1.5" fill="#b9975b"/><path d="M12 22q7 8 14 0"/></svg><div><h3>It's Stress Free</h3><p>Nam nec tellus a odio tincidunt auctor sed non elit eu mauris vitae erat as well consequat auctor eu in elit.</p></div></div>
      <div class="feature"><svg width="38" height="38" viewBox="0 0 38 38" fill="none" stroke="#b9975b" stroke-width="2"><circle cx="19" cy="21" r="13"/><path d="M19 13v8l5 4M6 8l6-4M32 8l-6-4"/></svg><div><h3>It's Accurate</h3><p>Nam nec tellus a odio tincidunt auctor sed non elit eu mauris vitae erat as well consequat auctor eu in elit.</p></div></div>
      <div class="feature"><svg width="38" height="38" viewBox="0 0 38 38" fill="none" stroke="#b9975b" stroke-width="2"><path d="M14 28V8l18-4v20"/><circle cx="10" cy="28" r="4"/><circle cx="28" cy="24" r="4"/></svg><div><h3>Greater Choice of Musics</h3><p>Nam nec tellus a odio tincidunt auctor sed non elit eu mauris vitae erat as well consequat auctor eu in elit.</p></div></div>
    </div>
  </div>
</section>

<section class="info">
  <div class="wrap">
    <div class="info-col">
      <h2 class="h2">Upcoming Events</h2>
      <div class="box">
        <div class="event"><span class="event-date">JUL 30</span><h4>Private Event - Aspendale (TBC)</h4><p>2:00 pm - 3:30 pm</p></div>
        <div class="event"><span class="event-date">AUG 05</span><h4>Corporate Event Harbourview Hotel</h4><p>7:30 pm - 9:30 pm</p></div>
        <div class="event"><span class="event-date">AUG 20</span><h4>Wedding Ceremony/Canapés Daylesford</h4><p>2:00 pm - 3:00 pm</p></div>
        <div class="event"><span class="event-date">SEP 16</span><h4>Wedding Ceremony/Canapés Daylesford</h4><p>@ 4:00 pm - 6:00 pm</p></div>
        <span class="all-events">VIEW ALL EVENTS ▸</span>
      </div>
    </div>
    <div class="info-col">
      <h2 class="h2">Testimonials</h2>
      <div class="testimonial">
        <div class="quote-mark">“</div>
        <blockquote>Tomas played together with Sofia (Cellist) and did an AMAZING job at Riverstone Estate! Having never met Tomas, I knew his work would be outstanding based on the samples he provided me. We decided to include the cello alongside the piano as we really wanted to include a string instrument (without having a string quartet!). He and Sofia were professional, punctual and played very well together. Would definitely recommend him for future events!</blockquote>
        <cite>ELEANOR</cite>
        <small>Riverstone Estate</small>
        <div class="dots"><i></i><i></i><i></i><i></i></div>
      </div>
    </div>
    <div class="info-col">
      <h2 class="h2">Make an Enquiry</h2>
      <div class="box enquiry">
        <p>Tomas Levett Pianist can be contacted by the following methods, or feel free to fill in the enquiry form.</p>
        <div class="field">Name</div>
        <div class="field">Email</div>
        <div class="field">Phone</div>
        <div class="field">Subject</div>
        <div class="field tall">Message</div>
        <span class="btn btn-gold">Enquire Now!</span>
      </div>
    </div>
  </div>
</section>

<section class="hire" aria-label="Hire call to action">
  <h2>HIRE AN AMAZING WEDDING PIANIST | EVENT PIANIST</h2>
  <p>Are you thinking about hiring a pianist for your wedding?</p>
  <div class="hire-actions"><span class="btn btn-gold">Book Now</span><span class="btn btn-dark">Get Your Price List</span></div>
</section>

<footer class="site-footer">
  <div class="wrap">
    <div class="footer-cols">
      <div class="footer-brand">
        <div class="brand"><span class="brand-dot"></span><div><div class="brand-name">TOMAS LEVETT</div><div class="brand-sub">Wedding &amp; Event Pianist</div></div></div>
        <address>220, lorem ipsum dolorossis,<br>dodis amet sit - 5489V<span>T: 1800 555 019<br>E: info@tomaslevett.com.au</span></address>
      </div>
      <div class="footer-links">
        <h4>Information</h4>
        <div class="lists">
          <ul><li>About Tomas</li><li>Events</li><li>Music</li><li>Video</li><li>Repertoire</li><li>Prices</li><li>Gallery</li></ul>
          <ul><li>Home</li><li>Contact</li><li>Suppliers</li><li>Hire Baby Grand Piano</li><li>FAQs</li><li>Testimonials</li><li>Buy CD</li></ul>
        </div>
      </div>
      <div class="footer-gram">
        <h4>Snapgram <span>@tomaslevett</span></h4>
        <div class="gram" role="img" aria-label="Grid of event photos"><div></div><div></div><div></div><div></div><div></div><div></div></div>
      </div>
    </div>
    <div class="socials">
      <span><i></i>Circlebook</span><span><i></i>Chirper</span><span><i></i>Snapgram</span><span><i></i>Pinboard</span><span><i></i>Linkwork</span><span><i></i>Viewtube</span><span><i></i>Subscribe Newsletter</span>
    </div>
    <div class="legal">
      <div>Copyright © 2017 TomasLevett. All Rights Reserved<br>Terms of Use | Privacy Policy | Sitemap</div>
      <div class="cards"><span>PayLine</span><span>CardOne</span><span>Duocard</span><span>Amcard</span></div>
    </div>
  </div>
</footer>

</body>
</html>
```